New solo practice law firm is looking for an elegant, professional, and interactive web design

I need a web design and developer for a new small law firm in Sacramento, California called Dorian Kessly Law, A Professional Corporation. I am a trial lawyer who represents average people facing difficult litigation disputes, including criminal defense as a former prosecutor and civil litigation as a civil litigator. Criminal defense includes domestic violence, battery, assault, drug possession, theft, DUI, etc. Civil litigation includes business disputes, property disputes, employment disputes, family law disputes, and immigration issues. I would like to see web designs that incorporate my logo and use the logo's navy blue and gold colors. I have uploaded the files of my logo to this brief. Please only use the navy blue and gold version. Overall, I want the design to look firm, professional, and elegant.

I plan on having the following pages on my website: (1) Home, (2) Dorian Kessly, (3) Practice Areas, (4) Insights, (5) Contact. I've hand drawn a preliminary sketch concept of what I envision the home page's layout to look like (attached with a text version). I would like your design to keep a similar layout for the homepage and incorporate my logo's colors within it but I am open to creative layout alternatives/ideas. I would like the other pages to have a similar look and feel as the home page. Some of the areas currently in my sketch do not have the full text. You can insert other text for now and I will provide the winner the full text.

In terms of the pictures on the website, I enjoy images of courthouses, columns (example attached but I cannot use this one), and, if possible, images from Sacramento, CA in my background (headshot attached). A plus would be live images that move and also sections of the webpage moving in the viewers view as they scroll down on the page. Also, it would be great to have my logo act as the tab for the website. I can provide other versions of the logo if needed.

I look forward to seeing your Wordpress designs!

People needing legal representation.

Law

Coded - Design and coding required

5+ page

Serif

• Incorporate my logo and my logo's colors.
• Live pictures and images appearing as viewers scroll on page.

```html
<!DOCTYPE html>
<html lang="en">
<head>
<meta charset="utf-8">
<title>Dorian Kessly Law</title>
<link href="https://fonts.googleapis.com/css2?family=Poppins:wght@300;400;500;600;700&family=Roboto:wght@400;500&display=swap" rel="stylesheet">
<style>
:root{
  --gold:#a88f5f;
  --gold-soft:#b89f6f;
  --navy:#1b2340;
  --navy-deep:#1d2746;
  --ink:#2b2b2b;
  --muted:#6d6d6d;
  --grey-band:#f3f3f3;
  --white:#ffffff;
}
*{margin:0;padding:0;box-sizing:border-box}
html,body{width:1200px;height:3042px;overflow:hidden}
body{position:relative;font-family:"Poppins",sans-serif;color:var(--ink);background:var(--white)}
.abs{position:absolute}

/* top bar */
.topbar{left:0;top:0;width:1200px;height:53px;background:var(--gold)}
.topbar .item{display:flex;align-items:center;gap:12px;color:var(--white);font-size:13.5px;line-height:19px;font-weight:500}
.topbar .icon{width:40px;height:40px;border-radius:50%;background:var(--navy);display:flex;align-items:center;justify-content:center}

/* nav */
.navbar{left:0;top:53px;width:1200px;height:109px;background:var(--white);border-bottom:1px solid #e6e6e6}
.brand{left:92px;top:18px;width:160px;height:130px;text-align:center}
.brand-disc{position:absolute;left:30px;top:0;width:100px;height:100px;border-radius:50%;background:var(--white)}
.brand-name{position:absolute;left:0;top:108px;width:160px;font-size:11px;letter-spacing:1.5px;color:var(--gold);font-weight:400}
.brand-sub{position:absolute;left:0;top:124px;width:160px;font-size:5.5px;letter-spacing:1.2px;color:var(--gold)}
.nav-links{left:428px;top:115px;display:flex;gap:28px;font-size:13.5px;letter-spacing:.5px;color:#333}
.lang{left:994px;top:114px;display:flex;align-items:center;gap:6px;font-size:13.5px;color:#333}

/* hero */
.hero{left:0;top:162px;width:1200px;height:599px;background:linear-gradient(180deg,#3a3f6d 0%,#4a4f7e 40%,#3b4366 62%,#253048 100%);overflow:hidden}
.hero-scene{position:absolute;left:0;top:0;width:1200px;height:599px;background:linear-gradient(180deg,rgba(120,110,150,.0) 30%,rgba(60,70,90,.45) 60%,rgba(30,40,55,.7) 100%)}
.hero-portrait{position:absolute;left:790px;top:30px;width:300px;height:569px;background:linear-gradient(180deg,#6b5a54 0%,#1c1d22 35%,#141519 100%);border-radius:140px 140px 0 0}
.hero-ghost{position:absolute;left:420px;top:40px;font-size:88px;font-weight:400;color:rgba(255,255,255,.35);white-space:nowrap}
.hero h1{position:absolute;left:110px;top:176px;font-size:51px;font-weight:600;color:var(--white)}
.hero p{position:absolute;left:111px;top:252px;width:510px;font-size:14.5px;line-height:31px;color:var(--white)}
.btn-gold{position:absolute;left:111px;top:359px;width:180px;height:51px;border-radius:6px;background:var(--gold);color:var(--white);font-size:16.5px;font-weight:500;display:flex;align-items:center;justify-content:center}
.slider-dots{position:absolute;left:550px;top:554px;display:flex;gap:8px}
.slider-dots span{display:block;height:20px;border-radius:10px;background:var(--white)}

/* intro */
.section-title{width:1200px;text-align:center;font-weight:600}
.intro-title{left:0;top:835px;font-size:35px;color:var(--gold)}
.intro-text{left:0;top:896px;width:1200px;text-align:center;font-size:14px;line-height:31px;color:#444}
.divider{display:flex;align-items:center;gap:10px;justify-content:center;width:1200px;left:0}
.divider .bar{width:48px;height:4px;background:var(--navy)}
.divider .dots{display:flex;gap:3px}
.divider .dots i{display:block;width:5px;height:4px;background:var(--gold)}
.area{width:186px;text-align:center}
.area .disc{width:186px;height:186px;border-radius:50%;border:1.5px solid var(--gold);padding:8px}
.area .disc div{width:100%;height:100%;border-radius:50%}
.area .label{margin-top:16px;font-size:16px;font-weight:600;color:var(--gold)}

/* about band */
.about-band{left:0;top:1324px;width:1200px;height:618px;background:var(--grey-band)}
.about-title{left:0;top:1359px;font-size:31px;color:#2a2a2a}
.about-lead{left:150px;top:1440px;width:900px;text-align:center;font-size:14.5px;line-height:31px;color:#444}
.about-photo-back{left:0;top:1552px;width:517px;height:22px;background:#a7a9b1}
.about-photo-back2{left:0;top:1563px;width:525px;height:12px;background:var(--navy)}
.about-photo{left:0;top:1574px;width:534px;height:422px;background:linear-gradient(160deg,#b29c6e 0%,#a58c5d 60%,#9c8456 100%);box-shadow:0 4px 10px rgba(0,0,0,.15)}
.about-photo .figure{position:absolute;left:210px;top:-24px;width:230px;height:446px;background:linear-gradient(180deg,#6b5a54 0%,#1c1d22 28%,#15161a 100%);border-radius:110px 110px 0 0}
.about-photo .vertical{position:absolute;left:142px;top:50px;writing-mode:vertical-rl;font-size:44px;color:rgba(255,255,255,.38);white-space:nowrap}
.about-head{left:625px;top:1548px;font-size:22px;font-weight:500;color:#3a3a3a}
.about-copy{left:625px;width:470px;font-size:13.5px;line-height:28.5px;color:#777}
.check{left:625px;display:flex;align-items:center;gap:6px;font-size:15.5px;color:#666}
.btn-navy{left:623px;top:1863px;width:180px;height:51px;border-radius:5px;background:var(--navy);color:var(--white);font-size:16.5px;font-weight:500;display:flex;align-items:center;justify-content:center;box-shadow:0 3px 8px rgba(0,0,0,.25)}

/* contact */
.contact-head{left:110px;top:2125px;font-size:24px;font-weight:600;line-height:38px;color:#2a2a2a}
.contact-head em{font-style:normal;color:var(--gold)}
.contact-copy{left:111px;top:2219px;width:430px;font-size:12.5px;line-height:26.5px;color:#666}
.contact-link{left:112px;top:2350px;font-size:15px;color:var(--gold);border-bottom:1px solid var(--gold);padding-bottom:1px}
.field{left:626px;width:490px;border-bottom:1px solid #bdbdbd;font-family:"Roboto",sans-serif;font-size:13.5px;color:#333;padding-bottom:10px}
.btn-submit{left:626px;top:2365px;width:223px;height:58px;border-radius:29px;background:var(--gold);color:var(--white);font-size:17px;font-weight:600;display:flex;align-items:center;justify-content:center;box-shadow:0 4px 8px rgba(0,0,0,.18)}

/* footer */
.footer{left:0;top:2510px;width:1200px;height:532px;background:linear-gradient(180deg,#1f2a4c 0%,#1b2545 100%);color:var(--white);font-family:"Roboto",sans-serif}
.social{display:flex;gap:8px;position:absolute;left:111px;top:52px}
.social span{width:44px;height:44px;background:var(--gold)}
.f-contact{position:absolute;display:flex;gap:14px}
.f-contact h4{font-family:"Poppins",sans-serif;font-size:15.5px;font-weight:600}
.f-contact p{font-size:13.5px;line-height:23px;margin-top:2px}
.f-rule{position:absolute;left:111px;width:978px;height:1px;background:rgba(255,255,255,.55)}
.f-col{position:absolute}
.f-col h3{font-family:"Poppins",sans-serif;font-size:20.5px;font-weight:500;margin-bottom:16px}
.f-col ul{list-style:none;font-size:13.5px;line-height:31px}
.f-col li::before{content:"";display:inline-block;border-left:4px solid var(--white);border-top:3.5px solid transparent;border-bottom:3.5px solid transparent;margin-right:8px;vertical-align:1px}
.f-col ul.plain li::before{display:none}
.f-firm{position:absolute;left:111px;top:208px}
.f-firm h3{font-family:"Poppins",sans-serif;font-size:17.5px;font-weight:600;line-height:30px}
.f-firm p{margin-top:18px;width:320px;font-size:13.5px;line-height:27.5px}
.copyright{position:absolute;left:0;top:488px;width:1200px;text-align:center;font-size:14.5px}
</style>
</head>
<body>

<!-- top bar -->
<div class="abs topbar">
  <div class="abs item" style="left:589px;top:7px">
    <div class="icon"><svg width="16" height="20" viewBox="0 0 16 20"><path d="M8 0a8 8 0 0 0-8 8c0 6 8 12 8 12s8-6 8-12a8 8 0 0 0-8-8zm0 11a3 3 0 1 1 0-6 3 3 0 0 1 0 6z" fill="#fff"/></svg></div>
    <div>2750 HARBOR POINT DR SUITE<br>#210 FAIRVIEW, CA 95700</div>
  </div>
  <div class="abs item" style="left:898px;top:7px">
    <div class="icon"><svg width="18" height="18" viewBox="0 0 24 24"><path d="M6.6 10.8a15.1 15.1 0 0 0 6.6 6.6l2.2-2.2a1 1 0 0 1 1-.25 11.4 11.4 0 0 0 3.6.57 1 1 0 0 1 1 1V20a1 1 0 0 1-1 1A17 17 0 0 1 3 4a1 1 0 0 1 1-1h3.5a1 1 0 0 1 1 1c0 1.25.2 2.45.57 3.57a1 1 0 0 1-.25 1z" fill="#fff"/></svg></div>
    <div>FREE CONSULTATION<br>(916) 555-0142</div>
  </div>
</div>

<!-- nav -->
<div class="abs navbar"></div>
<div class="abs brand">
  <div class="brand-disc"></div>
  <div class="brand-name">DORIAN KESSLY LAW</div>
  <div class="brand-sub">A PROFESSIONAL CORPORATION</div>
</div>
<nav class="abs nav-links">
  <span>HOME</span><span>DORIAN KESSLY</span><span>PRACTICE AREAS v</span><span>INSIGHTS</span><span>CONTACT</span>
</nav>
<div class="abs lang">
  <svg width="18" height="18" viewBox="0 0 18 18"><circle cx="9" cy="9" r="9" fill="#d33"/><rect x="0" y="4" width="18" height="2" fill="#fff"/><rect x="0" y="8" width="18" height="2" fill="#fff"/><rect x="0" y="12" width="18" height="2" fill="#fff"/><path d="M9 0A9 9 0 0 0 0 9h9z" fill="#2b3d8f"/></svg>
  <span>ENGLISH</span>
  <svg width="8" height="5" viewBox="0 0 8 5"><path d="M0 0h8L4 5z" fill="#333"/></svg>
</div>

<!-- hero -->
<section class="abs hero">
  <div class="hero-scene" role="img" aria-label="Dusk view of the Sacramento skyline across the river"></div>
  <div class="hero-ghost">Dorian Kessly</div>
  <div class="hero-portrait" role="img" aria-label="Portrait of Dorian Kessly in a dark suit"></div>
  <h1>Dorian Kessly Law</h1>
  <p>Dorian Kessly Law is a law firm serving the Sacramento, Yolo, San Joaquin, Solano and&nbsp; Stanislaus Counties. We represent clients in a wide array of criminal, civil, family law, and&nbsp; immigration cases.</p>
  <div class="btn-gold">Get Started</div>
  <div class="slider-dots"><span style="width:38px"></span><span style="width:56px"></span></div>
</section>

<!-- intro -->
<h2 class="abs section-title intro-title">CRIMINAL AND CIVIL TRIAL LAWYERS</h2>
<p class="abs intro-text">Dorian Kessly Law is a law firm serving the Sacramento, Yolo, San Joaquin, Solano and&nbsp; Stanislaus Counties.<br>We represent clients in a wide array of criminal, civil, family law, and&nbsp; immigration cases</p>
<div class="abs divider" style="top:977px"><span class="bar"></span><span class="dots"><i></i><i></i><i></i></span><span class="bar"></span></div>

<div class="abs area" style="left:164px;top:1021px">
  <div class="disc"><div role="img" aria-label="Handcuffed hands on a desk" style="background:linear-gradient(150deg,#3a3a44,#7a4a3a 55%,#5a3a30)"></div></div>
  <div class="label">Criminal Defense</div>
</div>
<div class="abs area" style="left:393px;top:1021px">
  <div class="disc"><div role="img" aria-label="Hand placing a chess piece on a city model" style="background:linear-gradient(180deg,#f2f2f2,#c9c9c9 55%,#2a2a2a)"></div></div>
  <div class="label">Civil Litigation</div>
</div>
<div class="abs area" style="left:622px;top:1021px">
  <div class="disc"><div role="img" aria-label="Stamp over a passport" style="background:linear-gradient(135deg,#d9c3a0,#8aa0b8 45%,#1f2b4a)"></div></div>
  <div class="label">Immigration</div>
</div>
<div class="abs area" style="left:851px;top:1021px">
  <div class="disc"><div role="img" aria-label="Lawyer meeting with clients at a table" style="background:linear-gradient(180deg,#e8ecef,#bfc6cc 50%,#2d2f35)"></div></div>
  <div class="label">Family Law</div>
</div>

<!-- about -->
<div class="abs about-band"></div>
<h2 class="abs section-title about-title">READY, RELIABLE, AND EXPERIENCED</h2>
<div class="abs divider" style="top:1418px"><span class="bar"></span><span class="dots"><i></i><i></i><i></i></span><span class="bar"></span></div>
<p class="abs about-lead">Lorem ipsum dolor sit amet, consectetur adipiscing elit, sed do eiusmod tempor incididunt ut labore et dolore magna aliqua. Ut enim ad minim veniam, quis nostrud exercitation ullamco laboris nisi ut aliquip ex ea commodo consequat.</p>

<div class="abs about-photo-back"></div>
<div class="abs about-photo-back2"></div>
<div class="abs about-photo">
  <div class="vertical">Dorian Kessly</div>
  <div class="figure" role="img" aria-label="Portrait of Dorian Kessly in a dark suit"></div>
</div>

<h3 class="abs about-head">Lorem ipsum dolor sit amet, consectetur</h3>
<p class="abs about-copy" style="top:1596px">Sed ut perspiciatis unde omnis iste natus error sit voluptatem accusantium doloremque laudantium, totam rem aperiam, eaque ipsa quae ab illo inventore veritatis et quasi architecto</p>
<p class="abs about-copy" style="top:1698px">Sed ut perspiciatis unde omnis iste natus error sit voluptatem accusantium doloremque laudantium,</p>
<div class="abs check" style="top:1782px"><svg width="14" height="14" viewBox="0 0 14 14"><circle cx="7" cy="7" r="7" fill="#a88f5f"/><path d="M3.8 7.2l2.2 2.2 4.2-4.4" stroke="#fff" stroke-width="1.8" fill="none"/></svg>Lorem ipsum dolor sit amet, consectetur adipiscing</div>
<div class="abs check" style="top:1812px"><svg width="14" height="14" viewBox="0 0 14 14"><circle cx="7" cy="7" r="7" fill="#a88f5f"/><path d="M3.8 7.2l2.2 2.2 4.2-4.4" stroke="#fff" stroke-width="1.8" fill="none"/></svg>Lorem ipsum dolor sit amet, consectetur adipiscing</div>
<div class="abs btn-navy">About Dorian</div>

<!-- contact -->
<h2 class="abs contact-head">When you contact <em>Dorian Kessly</em> Law<br>for a free consultation</h2>
<p class="abs contact-copy">Lorem ipsum dolor sit amet, consectetur adipiscing elit, sed do eiusmod tempor incididunt ut labore et dolore magna aliqua. Ut enim ad minim veniam, quis nostrud exercitation ullamco laboris nisi ut aliquip ex ea commodo consequat.</p>
<div class="abs contact-link">CONTACT US NOW</div>

<div class="abs field" style="top:2085px">Name</div>
<div class="abs field" style="top:2143px">Email Address</div>
<div class="abs field" style="top:2203px">Phone Number</div>
<div class="abs field" style="top:2263px;height:70px">Message</div>
<div class="abs btn-submit">SUBMIT</div>

<!-- footer -->
<footer class="abs footer">
  <div class="social"><span></span><span></span><span></span></div>

  <div class="f-contact" style="left:328px;top:52px">
    <svg width="32" height="42" viewBox="0 0 16 21"><path d="M8 0a8 8 0 0 0-8 8c0 6 8 13 8 13s8-7 8-13a8 8 0 0 0-8-8zm0 11a3 3 0 1 1 0-6 3 3 0 0 1 0 6z" fill="#a88f5f"/></svg>
    <div><h4>Visit our Location</h4><p>2750 Harbor Point Dr.<br>Suite #210 Fairview, CA 95700</p></div>
  </div>
  <div class="f-contact" style="left:603px;top:52px">
    <svg width="44" height="42" viewBox="0 0 24 24"><path d="M6.6 10.8a15.1 15.1 0 0 0 6.6 6.6l2.2-2.2a1 1 0 0 1 1-.25 11.4 11.4 0 0 0 3.6.57 1 1 0 0 1 1 1V20a1 1 0 0 1-1 1A17 17 0 0 1 3 4a1 1 0 0 1 1-1h3.5a1 1 0 0 1 1 1c0 1.25.2 2.45.57 3.57a1 1 0 0 1-.25 1z" fill="#a88f5f"/></svg>
    <div><h4>Give us a Call</h4><p>916-555-0187</p></div>
  </div>
  <div class="f-contact" style="left:830px;top:52px">
    <svg width="44" height="34" viewBox="0 0 44 34" style="margin-top:6px"><rect width="44" height="34" rx="3" fill="#a88f5f"/><path d="M2 3l20 16L42 3" stroke="#1d2746" stroke-width="2.5" fill="none"/></svg>
    <div><h4>Send us a Message</h4><p>info@DorianKessly.com</p></div>
  </div>

  <div class="f-rule" style="top:152px"></div>

  <div class="f-firm">
    <h3>Dorian Kessly Law<br>A Professional Corporation</h3>
    <p>Lorem ipsum dolor sit amet, consectetur adipiscing elit, sed do eiusmod tempor incididunt ut labore et dolore magna aliqua. Ut enim ad minim veniam, quis nostru</p>
  </div>
  <div class="f-col" style="left:523px;top:208px">
    <h3>Navigation</h3>
    <ul><li>Home</li><li>Dorian Kessly</li><li>Practice Areas</li><li>Insights</li><li>Contact</li></ul>
  </div>
  <div class="f-col" style="left:725px;top:208px">
    <h3>Our Services</h3>
    <ul><li>Criminal Defense</li><li>Civil Litigation</li><li>Immigration</li><li>Family Law</li></ul>
  </div>
  <div class="f-col" style="left:966px;top:208px">
    <h3>Help Us</h3>
    <ul class="plain"><li>Privacy Policy</li><li>Terms &amp; Conditions</li></ul>
  </div>

  <div class="f-rule" style="top:440px"></div>
  <div class="copyright">© 2021 All Rights Reserved</div>
</footer>

</body>
</html>
```